Steps to get a free fence estimate

Hi! I need a new flyer in the similar design / style that you created previously for us! I would like this one to showcase the steps to get a free estimate.
There are several options to obtain a free fence quote for your fence installation or to buy fence materials:
1) In-Person - In-person quotes are available for fence installations only. Call, email or message us online to schedule an in-person measurement at your property.
2) Virtual Quotes - Send us your lot survey, fence layout diagram with dimensions, or measure your property online using our Digital Boundary Sizing Wizard. We can review the dimensions to provide a site-unseen quote. You can also call us with your project information for a quote via phone.
3) Competitor Quotes - Send us the quotes from qualified competitors for price comparisons. Competitor quotes must have fence style, footage, and other project information.
What information do we need to give you a free estimate?
Fence footage - how many feet of fencing do you need?
Fence style - what fence style and material would you like quoted?
Fence placement - does the fence need to be installed in concrete or asphalt surfaces? or will it be installed in normal dirt areas?
Gate information - do you need any single person walk through gates, or a larger double gate? (walk gates can be 3FT, 4FT and 5FT wide - 5FT wide is wide enough for a riding lawn mower to get through. double gates can be 8FT, 10FT and 12FT wide.)
For installation quotes, please let us know any additional information such as if there is any existing fencing to remove, obstacles in the path of the fence line or if the fence has to be installed on top of concrete/asphalt surfaces.
We make the fence quoting process easy and simple!
Lifetime warranty on workmanship, labor and manufacturer's lifetime warranty on materials.
---
This flyer only needs to discuss the steps to obtaining a free fence estimate for our customers.

```html
<!DOCTYPE html>
<html lang="en">
<head>
<meta charset="utf-8">
<title>Steps to Get a Free Fence Estimate</title>
<link rel="stylesheet" href="https://fonts.googleapis.com/css2?family=Montserrat:wght@400;500;800&family=Open+Sans:wght@700&display=swap">
<style>
  :root {
    --sky-top: #d9d9d9;
    --sky-bottom: #f2f2f2;
    --wood-light: #ecd6a6;
    --wood-mid: #dcbd83;
    --wood-dark: #c9a468;
    --badge-gold: #d6b36f;
    --badge-frame: #ffffff;
    --badge-edge: #c9c9c9;
    --band-light: rgba(255, 255, 255, 0.55);
    --band-tan: rgba(201, 164, 104, 0.35);
    --ink: #121212;
    --footer-ink: #ffffff;
  }
  * { margin: 0; padding: 0; box-sizing: border-box; }
  html, body { width: 848px; height: 1200px; overflow: hidden; }
  body { font-family: "Montserrat", sans-serif; color: var(--ink); }
  .flyer {
    position: relative;
    width: 848px;
    height: 1200px;
    overflow: hidden;
    background: linear-gradient(180deg, var(--sky-top) 0%, var(--sky-bottom) 60%);
  }
  .fence-backdrop { position: absolute; inset: 0; }
  .headline {
    position: absolute;
    top: 36px;
    left: 0;
    width: 848px;
    text-align: center;
  }
  .headline__title {
    font-weight: 800;
    font-size: 52px;
    line-height: 53px;
    letter-spacing: 0.5px;
  }
  .headline__lede {
    margin-top: 12px;
    font-weight: 400;
    font-size: 22px;
    line-height: 31px;
  }
  .band { position: absolute; left: 253px; right: 0; }
  .band--light { background: var(--band-light); }
  .band--tan { background: var(--band-tan); }
  .badge { position: absolute; left: 90px; width: 168px; height: 240px; }
  .badge__label {
    font-family: "Open Sans", sans-serif;
    font-weight: 700;
    font-size: 19px;
    fill: #ffffff;
  }
  .option-text {
    position: absolute;
    left: 292px;
    font-size: 17px;
    line-height: 26.5px;
    font-weight: 500;
  }
  .footer-note {
    position: absolute;
    top: 1096px;
    left: 70px;
    width: 708px;
    text-align: center;
    color: var(--footer-ink);
    font-size: 13.6px;
    line-height: 21.5px;
  }
</style>
</head>
<body>
<main class="flyer">
  <svg class="fence-backdrop" width="848" height="1200" viewBox="0 0 848 1200" role="img" aria-label="Photo of a pale wooden picket fence stepping down against a cloudy sky">
    <defs>
      <linearGradient id="wood" x1="0" y1="0" x2="1" y2="1">
        <stop offset="0" stop-color="var(--wood-light)"/>
        <stop offset="0.55" stop-color="var(--wood-mid)"/>
        <stop offset="1" stop-color="var(--wood-dark)"/>
      </linearGradient>
    </defs>
    <polygon fill="url(#wood)" points="0,112 46,138 92,188 117,178 210,262 236,255 307,289 330,322 350,318 420,350 480,430 500,422 530,450 600,482 625,478 700,530 712,526 760,568 768,564 848,596 848,1200 0,1200"/>
  </svg>

  <header class="headline">
    <h1 class="headline__title">THERE ARE<br>SEVERAL OPTIONS</h1>
    <p class="headline__lede">to obtain a free fence quote for your fence<br>installation or to buy fence materials:</p>
  </header>

  <div class="band band--light" style="top:357px;height:201px"></div>
  <div class="band band--tan" style="top:558px;height:38px"></div>
  <div class="band band--light" style="top:596px;height:204px"></div>
  <div class="band band--tan" style="top:800px;height:41px"></div>
  <div class="band band--light" style="top:841px;height:204px"></div>

  <svg class="badge" style="top:357px" viewBox="0 0 168 240">
    <polygon fill="var(--badge-edge)" points="3,41 13,39 13,235 3,237"/>
    <polygon fill="var(--badge-frame)" points="13,39 163,0 163,203 13,235"/>
    <polygon fill="var(--badge-gold)" points="13,45 150,19 150,188 13,218"/>
    <rect x="46" y="62" width="66" height="70" fill="#e6cc97" role="img" aria-label="Handshake icon"/>
    <text class="badge__label" x="82" y="186" text-anchor="middle" transform="rotate(-11 82 186)">In-Person</text>
  </svg>
  <p class="option-text" style="top:364px">In-person quotes are<br>available for fence<br>installations only. Call, email<br>or message us online to<br>schedule an in-person<br>measurement at your<br>property.</p>

  <svg class="badge" style="top:597px" viewBox="0 0 168 240">
    <polygon fill="var(--badge-edge)" points="3,41 13,39 13,235 3,237"/>
    <polygon fill="var(--badge-frame)" points="13,39 163,0 163,203 13,235"/>
    <polygon fill="var(--badge-gold)" points="13,45 150,19 150,188 13,218"/>
    <rect x="30" y="60" width="100" height="66" fill="#e6cc97" role="img" aria-label="Tape measure icon"/>
    <text class="badge__label" x="82" y="170" text-anchor="middle" transform="rotate(-11 82 170)">Virtual</text>
    <text class="badge__label" x="82" y="194" text-anchor="middle" transform="rotate(-11 82 194)">Quotes</text>
  </svg>
  <p class="option-text" style="top:615px">Send us your lot survey, fence layout diagram<br>with dimensions, or measure your property<br>online using our Digital Boundary Sizing Wizard.<br>We can review the dimensions to provide a<br>site-unseen quote. You can also call us with your<br>project information for a quote via phone.</p>

  <svg class="badge" style="top:840px" viewBox="0 0 168 240">
    <polygon fill="var(--badge-edge)" points="3,41 13,39 13,235 3,237"/>
    <polygon fill="var(--badge-frame)" points="13,39 163,0 163,203 13,235"/>
    <polygon fill="var(--badge-gold)" points="13,45 150,19 150,188 13,218"/>
    <rect x="36" y="46" width="92" height="92" fill="#e6cc97" role="img" aria-label="Magnifying glass beside a person icon"/>
    <text class="badge__label" x="84" y="174" text-anchor="middle" transform="rotate(-11 84 174)">Competitor</text>
    <text class="badge__label" x="84" y="198" text-anchor="middle" transform="rotate(-11 84 198)">Quotes</text>
  </svg>
  <p class="option-text" style="top:848px">Send us the quotes from<br>qualified competitors for<br>price comparisons.<br>Competitor quotes must<br>have fence style, footage,<br>and other project<br>information.</p>

  <p class="footer-note">Gate information - do you need any single person walk through gates, or a larger double gate? (walk gates can be 3FT, 4FT and 5FT wide - 5FT wide is wide enough for a riding lawn mower to get through. double gates can be 8FT, 10FT and 12FT wide.)</p>
</main>
</body>
</html>
```